Webpage for an exhibition

A classy and fun webpage required for a fashion and consumer exhibition show that will showcase fashion, fashion shows, art, home decor, food, pop up shops etc.
The exhibition is called the sunvale garden expo.
it will be held at a green city park.
Its a fashion and lifestyle show.There will be established and emerging brands who will exhibit from other parts of Africa at the show.

There will be fashion shows. music and others
See attached

This is a classy . fun and sophisticated show and clean.

See Orvanique week. Marlowe Velis week

Target Market(s)

Fashion and lifestyle concious individuals
young proffesionals -age 25- 60
industry fashion buyers
magazines, bloggers
media houses
students

Industry/Entity Type

Fashion

Font styles to use
Sans Serif

Requirements
Must have
• Web page must have gold .white, black.
use attached poster and logo colours.

Web page must have the following pages.
Home.about us.exhibitors.visitors.gallery.sponsors.contact us.
create a banner for advertising and sponsors. create it on the right hand side of the page or at the bottom.
Must have a slide show on home page. photos must move or alternate every 5 secs. Type of photos can be pictures of brands exhibiting. models.fashion showd.
Count down date and time to show.
Create twitter.facebook.instagram.youtube.

see attached
Nice to have
• Models must be black and white races. Dont worry if you have no models. Use nice modern pictures. for slide show use photos include the show poster.
Its the next big thing on the continent. The number one show.
Should not have
• No animals. No animal looking photos.

```html
<!DOCTYPE html>
<html lang="en">
<head>
<meta charset="utf-8">
<title>The Sunvale Garden Expo 2014</title>
<link rel="stylesheet" href="https://fonts.googleapis.com/css2?family=Cinzel:wght@600;700&family=Open+Sans:wght@300;400;600;700&display=swap">
<style>
:root{
  --ink:#111111;
  --panel:#6a6a6a;
  --gold:#e0a716;
  --gold-deep:#b98207;
  --gold-light:#f4c230;
  --white:#ffffff;
  --footer:#232323;
  --badge:#bdbdbd;
}
*{box-sizing:border-box;margin:0;padding:0}
html,body{width:782px;height:1200px;overflow:hidden;background:var(--ink)}
body{position:relative;font-family:"Open Sans",Arial,sans-serif;color:var(--white)}
.abs{position:absolute}
.brand{left:84px;top:16px;display:flex;align-items:center;gap:6px}
.brand-dot{width:36px;height:36px;border-radius:50%;background:var(--gold);flex:none}
.brand-name{font-size:8px;font-weight:600;line-height:1.2;color:var(--white);width:62px}
.main-nav{left:78px;top:79px;width:625px;height:40px;background:linear-gradient(180deg,var(--gold-light),var(--gold) 55%,var(--gold-deep));display:flex;align-items:center}
.main-nav a{font-family:"Cinzel",serif;font-weight:700;text-transform:uppercase;font-size:10px;color:#2a1c00;text-decoration:none;letter-spacing:.2px;white-space:nowrap}
.main-nav .current{background:#8f6204;color:#f7d76a;height:40px;width:75px;display:flex;align-items:center;justify-content:center;font-size:11px}
.main-nav .link{margin-left:25px}
.main-nav .link:first-of-type{margin-left:6px}
.hero{left:78px;top:119px;width:625px;height:223px;overflow:hidden;
  background:
   radial-gradient(ellipse 90px 120px at 90px 110px,rgba(40,20,10,.55),transparent),
   radial-gradient(ellipse 80px 120px at 230px 120px,rgba(30,40,60,.45),transparent),
   radial-gradient(ellipse 110px 90px at 560px 60px,rgba(120,150,60,.5),transparent),
   linear-gradient(100deg,#7a3a12 0%,#c8951e 22%,#d9b241 32%,#3d5a34 48%,#9a7a2a 62%,#b5762a 78%,#5a2c10 100%)}
.hero-caption{left:376px;top:59px;width:249px;height:103px;background:rgba(20,20,20,.5);padding:12px 0 0 25px}
.hero-caption .line1{font-size:21px;font-weight:700;line-height:1.2;white-space:nowrap}
.hero-caption .line2{font-size:31px;font-weight:300;color:var(--gold-light);line-height:1.1;white-space:nowrap}
.hero-arrows{right:10px;bottom:10px}
.tagline{left:0;top:358px;width:782px;text-align:center;font-size:17px;font-weight:300}
.card{width:150px}
.card .photo{height:120px}
.ph1{background:radial-gradient(ellipse at 30% 50%,#5b4a3a,transparent 60%),linear-gradient(160deg,#2c3a55,#1a2233 60%,#5a5f6a)}
.ph2{background:radial-gradient(ellipse at 50% 45%,#8a7066,transparent 55%),linear-gradient(135deg,#eeeeee,#2a2a2a 45%,#555 100%)}
.ph3{background:radial-gradient(ellipse at 30% 60%,#3a3a3a,transparent 50%),linear-gradient(170deg,#d0d0d0,#8a8a8a 50%,#444)}
.ph4{background:radial-gradient(ellipse at 30% 60%,#6b4a2a,transparent 55%),radial-gradient(ellipse at 75% 50%,#8a7a60,transparent 55%),linear-gradient(180deg,#a7b6c4,#4a3a30 60%,#2a2a2a)}
.ph5{background:radial-gradient(ellipse at 50% 55%,#1a1a1a,transparent 60%),linear-gradient(150deg,#8a8a8a,#333 55%,#1c1c1c)}
.ph6{background:radial-gradient(ellipse at 50% 65%,#2a2a2a,transparent 45%),linear-gradient(180deg,#f0f0f0,#b8bec4 45%,#7a7f84)}
.card .body{padding:9px 9px 0 10px}
.grey{background:var(--panel)}
.gold{background:var(--gold)}
.card h2{font-size:11.5px;font-weight:700;line-height:1.15}
.card .sub{font-size:8.5px;font-weight:400}
.card p{font-size:7.4px;line-height:1.6;margin-top:11px}
.card ul{list-style:none;margin-top:6px;padding-left:3px}
.card li{font-size:7.4px;line-height:1.65;padding-left:10px;position:relative;margin-bottom:3px}
.card li::before{content:"›";position:absolute;left:0;top:-1px;font-size:9px}
.card li.plain::before{content:none}
.card .lead{font-size:7.4px;font-weight:700;margin-top:10px;padding-left:10px}
.info{left:550px;top:405px;width:150px;height:284px;background:var(--gold);padding:6px}
.info .logo-box{height:60px;background:var(--ink);display:flex;align-items:center;padding-left:8px;gap:5px;margin-bottom:8px}
.info dt{font-size:8.5px;font-weight:700;margin-top:10px}
.info dd{font-size:8.5px;line-height:1.15}
.team{left:556px;top:700px;width:142px}
.team h3{font-size:11.5px;font-weight:400;color:var(--gold);margin-bottom:10px}
.team p{font-size:7.5px;line-height:1.7}
.team a{color:var(--gold-light);font-weight:700;text-decoration:none}
.sponsors{left:550px;top:834px;width:150px;height:210px;background:var(--white);color:#333;text-align:center;padding-top:13px}
.sponsors h3{font-size:11.5px;font-weight:400;margin-bottom:16px}
.sponsor-grid{display:grid;grid-template-columns:repeat(3,30px);gap:12px 15px;justify-content:center}
.sponsor-grid span{height:22px;background:var(--badge)}
.sponsor-grid span:nth-child(3n+2){border-radius:50%}
.site-footer{left:0;top:1086px;width:782px;height:114px;background:var(--footer)}
.social{left:347px;top:19px;display:flex;gap:4px}
.social span{width:20px;height:20px;border-radius:50%;border:1.5px solid var(--gold)}
.social .s1{background:#2a78b8}
.social .s2{background:#3b4f86}
.social .s3{background:#b8251f}
.social .s4{background:#5a3a1a}
.footer-nav{left:0;top:54px;width:782px;text-align:center;font-size:9.5px;font-weight:700}
.footer-nav a{color:var(--white);text-decoration:none;margin:0 11px}
.copyright{left:0;top:78px;width:782px;text-align:center;font-size:9px;font-weight:700}
</style>
</head>
<body>
<header>
  <div class="abs brand"><span class="brand-dot"></span><span class="brand-name">The Sunvale Garden Expo 2014</span></div>
  <nav class="abs main-nav">
    <a class="current" href="#">Home</a>
    <a class="link" href="#">About Us</a>
    <a class="link" href="#">Exhibitors</a>
    <a class="link" href="#">Visitors</a>
    <a class="link" href="#">Gallery</a>
    <a class="link" href="#">Sponsors</a>
    <a class="link" href="#">Contact Us</a>
  </nav>
  <section class="abs hero" role="img" aria-label="Slideshow photo of models in colourful African print fashion on a city street">
    <div class="abs hero-caption"><div class="line1">The Sunvale Garden</div><div class="line2">Expo 2014</div></div>
    <svg class="abs hero-arrows" width="40" height="20" viewBox="0 0 40 20" aria-hidden="true">
      <polyline points="11,3 4,10 11,17" fill="none" stroke="#fff" stroke-width="2.5"/>
      <polyline points="29,3 36,10 29,17" fill="none" stroke="#fff" stroke-width="2.5"/>
    </svg>
  </section>
</header>

<p class="abs tagline">“To help to develop and promote a better Africa“</p>

<main>
  <article class="abs card grey" style="left:82px;top:404px;height:285px">
    <div class="photo ph1" role="img" aria-label="Photo of fashion models on a train"></div>
    <div class="body">
      <h2>What is the<br>Sunvale Garden Expo?</h2>
      <p style="margin-top:20px">The Sunvale Garden Expo is an annual fashion and consumer exhibition initiative by Telmaris Group that connects brands and consumers in the Diaspora by bringing together some of the strongest brands to showcase to a global audience.</p>
    </div>
  </article>
  <article class="abs card gold" style="left:237px;top:404px;height:285px">
    <div class="photo ph2" role="img" aria-label="Black and white fashion portrait"></div>
    <div class="body">
      <h2>What will happen<br>at the consumer<br>exhibition?</h2>
      <p style="margin-top:9px">It will be a consumer "live" event where brands which meet a set criteria will be sourced all over Africa to present to a global audience in South Africa. Brands that will be sourced to exhibit will be passionate about what they do and their need to reach a wider audience.</p>
    </div>
  </article>
  <article class="abs card grey" style="left:393px;top:404px;height:285px">
    <div class="photo ph3" role="img" aria-label="Black and white photo of models at a casting"></div>
    <div class="body">
      <h2>Why join us<br><span class="sub">(for exhibitors)?</span></h2>
      <div class="lead">If you want to:</div>
      <ul style="margin-top:14px">
        <li>Gain regional market exposure</li>
        <li>Establish trade contacts</li>
        <li class="plain">Leverage on cost effective marketing</li>
        <li>Reach a wide target market</li>
      </ul>
    </div>
  </article>
  <aside class="abs info">
    <div class="logo-box"><span class="brand-dot" style="width:28px;height:28px"></span><span class="brand-name" style="font-size:7.5px">The Sunvale Garden Expo 2014</span></div>
    <dl>
      <dt>DATE:</dt><dd>19-22 September 2014</dd>
      <dt>VENUE:</dt><dd>In a vibrant Park<br>(Details to be shared closer to the date)</dd>
      <dt>TICKETS:</dt><dd>R100 per person</dd>
      <dt>For VIP Tickets:</dt><dd>please email<br>info@sunvalegardenexpo.com</dd>
      <dt style="margin-top:12px">TIME:</dt><dd>9am – 5pm</dd>
    </dl>
  </aside>

  <article class="abs card grey" style="left:82px;top:696px;height:348px">
    <div class="photo ph4" role="img" aria-label="Photo of models in patterned outfits"></div>
    <div class="body" style="padding-left:5px">
      <h2>Why attend?</h2>
      <p style="margin-top:2px;padding-left:3px;font-size:7.8px">To interact and socialise with entrepreneurs</p>
      <div class="lead" style="margin-top:12px;padding-left:18px">See what's new</div>
      <ul style="margin-top:14px;padding-left:10px">
        <li>Evaluate products and suppliers</li>
        <li>Keep abreast of industry and market developments</li>
        <li>Network/develop business contacts</li>
        <li>Solve specific problems</li>
      </ul>
    </div>
  </article>
  <article class="abs card gold" style="left:237px;top:696px;height:348px">
    <div class="photo ph5" role="img" aria-label="Black and white photo of three young men"></div>
    <div class="body">
      <h2>What will be the<br>Experience for the<br>exhibitor?</h2>
      <ul style="margin-top:12px;padding-left:12px">
        <li class="plain" style="padding-left:0">It will be highly targeted</li>
        <li>The buyer will come to you 3D sales &amp; promotion/ live demonstration platform</li>
        <li>Face to face contact - the most persuasive form of selling, and of building customer relationships.</li>
      </ul>
    </div>
  </article>
  <article class="abs card grey" style="left:393px;top:696px;height:348px">
    <div class="photo ph6" role="img" aria-label="Photo of business people meeting by a window"></div>
    <div class="body">
      <h2>Why Sponsor/ Partner<br>with us?</h2>
      <ul style="margin-top:18px">
        <li>To help us make a difference in Africa</li>
        <li>Maximise brand awareness and create preference</li>
        <li>Showcase your product and services to potential users</li>
        <li>Develop relationships with potential customers and strengthen relationships with current ones</li>
      </ul>
    </div>
  </article>

  <section class="abs team">
    <h3>OUR TEAM</h3>
    <p>The Sunvale Garden Expo has an amazing team of talent that is passionate about what we do. We are committed to excellence and a shared vision to create opportunities for development for a better Africa through our platform. <a href="#">Read More</a></p>
  </section>
  <section class="abs sponsors">
    <h3>SPONSORS</h3>
    <div class="sponsor-grid" aria-label="Sponsor badges">
      <span></span><span></span><span></span>
      <span></span><span></span><span></span>
      <span></span><span></span><span></span>
      <span></span><span></span><span></span>
    </div>
  </section>
</main>

<footer class="abs site-footer">
  <div class="abs social" aria-label="Social links"><span class="s1"></span><span class="s2"></span><span class="s3"></span><span class="s4"></span></div>
  <nav class="abs footer-nav">
    <a href="#">Home</a>|<a href="#">About Us</a>|<a href="#">Exhibitors</a>|<a href="#">Visitors</a>|<a href="#">Gallery</a>|<a href="#">Sponsors</a>|<a href="#">Contact Us</a>
  </nav>
  <p class="abs copyright">© 2014 CompanyName ,All Rights reserved</p>
</footer>
</body>
</html>
```